Oven Cleaning Business owner needs business card design

Hi there,
Would like for a business card to be designed for myself, the owner of a professional oven cleaning business on the Sunshine Coast.
Would like it to look sleek, and modern-ish. Bit creative is encouraged too.
Include following:
Name/title: Corin ter Haghe, Owner
Phone number: 1300 482 916
Email: info@hearthshinecrew.com.au
Website: www.hearthshinecrew.com.au

```html
<!DOCTYPE html>
<html lang="en">
<head>
<meta charset="utf-8">
<title>Hearthshine Crew – Business Card</title>
<link rel="stylesheet" href="https://fonts.googleapis.com/css2?family=Montserrat:wght@700;800&family=Cabin:wght@400&display=swap">
<style>
  :root {
    --stage: #d8d3cb;
    --card: #070808;
    --card-soft: #0c1112;
    --teal: #4bb8c2;
    --teal-faint: #13272a;
    --white: #f4f6f6;
    --rule: #1f5a5f;
  }
  * { box-sizing: border-box; margin: 0; padding: 0; }
  html, body { width: 1200px; height: 900px; overflow: hidden; }
  body {
    background: var(--stage);
    display: flex; flex-direction: column; align-items: center; justify-content: center;
    gap: 40px;
    font-family: "Cabin", "Helvetica Neue", sans-serif;
  }
  .card {
    position: relative;
    width: 640px; height: 366px;
    background: var(--card);
    overflow: hidden;
    box-shadow: 0 8px 24px rgba(0,0,0,.25);
  }

  /* Back side */
  .back-pattern {
    position: absolute; inset: 0;
    background: radial-gradient(circle at 50% 50%, var(--teal-faint) 0%, var(--card-soft) 55%, var(--card) 100%);
    opacity: .75;
  }
  .back-mark {
    position: absolute; right: 70px; top: 232px;
    display: flex; align-items: center; gap: 8px;
    font-family: "Montserrat", sans-serif; font-weight: 800;
    font-size: 13px; letter-spacing: .06em; text-transform: uppercase;
    color: var(--teal);
  }
  .back-mark .dot { width: 14px; height: 14px; border-radius: 50%; background: var(--teal); }

  /* Front side */
  .front-backdrop {
    position: absolute; left: 40px; bottom: -40px;
    width: 270px; height: 250px;
    border-radius: 50% 50% 46% 46%;
    background: radial-gradient(circle at 50% 55%, var(--teal-faint) 0%, rgba(19,39,42,.4) 60%, rgba(7,8,8,0) 100%);
  }
  .identity { position: absolute; left: 34px; top: 128px; }
  .identity .title { color: var(--white); font-size: 14px; letter-spacing: .02em; }
  .identity .name {
    font-family: "Montserrat", sans-serif; font-weight: 800;
    color: var(--teal); font-size: 19px; text-transform: uppercase; letter-spacing: .01em;
    margin-top: 2px;
  }
  .contacts {
    position: absolute; left: 350px; top: 110px;
    list-style: none; color: var(--white); font-size: 15px; line-height: 24px;
  }
  .contacts li { display: flex; align-items: center; gap: 8px; }
  .contacts svg { width: 14px; height: 14px; flex: none; }
  .divider {
    position: absolute; left: 350px; right: 30px; top: 196px;
    height: 1px; background: var(--rule);
  }
  .brand {
    position: absolute; left: 350px; top: 226px;
    display: flex; align-items: center; gap: 12px;
    font-family: "Montserrat", sans-serif; font-weight: 800;
    font-size: 26px; line-height: 1.05; text-transform: uppercase; letter-spacing: .04em;
    color: var(--white);
  }
  .brand .dot { width: 44px; height: 44px; border-radius: 50%; background: var(--teal); flex: none; }
</style>
</head>
<body>

  <section class="card card-back" aria-label="Card back">
    <div class="back-pattern" role="img" aria-label="Repeating faint brand pattern in dark teal"></div>
    <div class="back-mark"><span class="dot"></span>Hearthshine Crew</div>
  </section>

  <section class="card card-front" aria-label="Card front">
    <div class="front-backdrop" role="img" aria-label="Large faint brand decoration in dark teal"></div>

    <div class="identity">
      <p class="title">Owner</p>
      <h1 class="name">Corin ter Haghe</h1>
    </div>

    <ul class="contacts">
      <li>
        <svg viewBox="0 0 16 16" aria-hidden="true"><path fill="var(--teal)" d="M2 5c0-2 2-3 6-3s6 1 6 3l-3 1-1-2H6L5 6 2 5zm2 2h8l1 6H3l1-6zm4 1.5a2 2 0 100 4 2 2 0 000-4z"/></svg>
        1300 482 916
      </li>
      <li>
        <svg viewBox="0 0 16 16" aria-hidden="true"><rect x="1.5" y="4" width="13" height="9" rx="1" fill="none" stroke="var(--teal)" stroke-width="1.6"/><path d="M2 5l6 4.5L14 5" fill="none" stroke="var(--teal)" stroke-width="1.6"/></svg>
        info@hearthshinecrew.com.au
      </li>
      <li>
        <svg viewBox="0 0 16 16" aria-hidden="true"><circle cx="8" cy="8" r="6.2" fill="none" stroke="var(--teal)" stroke-width="1.5"/><ellipse cx="8" cy="8" rx="2.6" ry="6.2" fill="none" stroke="var(--teal)" stroke-width="1.2"/><path d="M2 8h12" stroke="var(--teal)" stroke-width="1.2"/></svg>
        www.hearthshinecrew.com.au
      </li>
    </ul>

    <div class="divider"></div>

    <div class="brand"><span class="dot"></span><span>Hearthshine<br>Crew</span></div>
  </section>

</body>
</html>
```